Looking to build a senior life alert web page

We definitely want to incorporate pictures of the product in which we're selling and want colors that resonate with the senior community. We're looking for something also clean and very easy to navigate. We're looking to pick a design immediately!
Based on something similar to that of our competition which can be located at the following
https://www.corvenhelpline.com/
https://www.trellowatch.com/

attached is the product we're selling

The name of our company is the elder harbor circle

Target Market(s)

Elderly people looking for a life alert device

Industry/Entity Type

Medical Equipment

Number of Pages Required

3 page

Font styles to use
Serif

Colors

Designer to choose colors to be used in the design.

Requirements
Must have
• Pictures of the product a nice UI experience that can be easily made mobile friendly
Nice to have
• Including area for video content maybe / friendly color LOGOS are attached for our company

```html
<!DOCTYPE html>
<html lang="en">
<head>
<meta charset="utf-8">
<title>Elder Harbor Circle</title>
<link rel="stylesheet" href="https://fonts.googleapis.com/css2?family=Poppins:wght@400;500;600;700&display=swap">
<style>
:root{
  --navy:#1b4a78;
  --navy-deep:#134473;
  --ink:#2b3a4a;
  --muted:#7b8794;
  --orange:#f29a1d;
  --orange-dark:#e3861a;
  --line:#e4e8ec;
  --white:#ffffff;
  --photo-grey:#dcdfe2;
}
*{box-sizing:border-box;margin:0;padding:0}
html,body{width:1200px;height:4350px;overflow:hidden;background:var(--white)}
body{font-family:'Poppins',sans-serif;color:var(--ink);position:relative}
.abs{position:absolute}
.btn{display:inline-flex;align-items:center;justify-content:center;gap:8px;font-weight:600;font-size:17px;border-radius:30px;text-decoration:none}
.btn-solid{background:var(--orange);color:var(--white)}
.btn-outline{border:2px solid var(--orange);color:var(--orange);background:var(--white)}
.photo{position:absolute}
.section-title{position:absolute;left:0;width:1200px;text-align:center;font-weight:700;color:var(--navy);font-size:36px}
.section-lede{position:absolute;left:200px;width:800px;text-align:center;font-size:15px;line-height:28px;color:var(--muted)}
.date-row{position:absolute;display:flex;align-items:flex-start;gap:16px}
.date{font-weight:700;color:var(--navy);font-size:17px;line-height:24px;text-align:center;padding-right:14px;border-right:3px solid var(--orange);min-width:80px}
.date-text{font-size:15px;line-height:26px;color:var(--ink)}
.pager{position:absolute;display:flex;gap:10px}
.pager span{width:34px;height:34px;border-radius:50%;display:flex;align-items:center;justify-content:center}
.pager .prev{background:#c9ced3}
.pager .next{background:var(--orange)}

/* header */
.site-header{top:0;left:0;width:1200px;height:82px;background:var(--white);display:flex;align-items:center;padding:0 40px}
.brand{display:flex;align-items:center;gap:10px;font-weight:700;color:var(--navy);font-size:22px}
.brand-dot{width:34px;height:34px;border-radius:50%;background:var(--orange)}
.main-nav{margin-left:auto;display:flex;gap:26px;font-size:16px;color:var(--ink)}
.header-phone{margin-left:40px;display:flex;align-items:center;gap:8px;font-weight:700;color:var(--navy);font-size:18px}
.header-login{margin-left:40px;height:40px;padding:0 22px;font-size:15px;border-radius:6px}

/* hero */
.hero{top:82px;left:0;width:1200px;height:552px}
.hero-title{left:663px;top:170px;width:420px;font-size:40px;line-height:48px;font-weight:700;color:var(--navy)}
.hero-text{left:663px;top:272px;width:420px;font-size:15px;line-height:28px;color:var(--ink)}
.hero-cta{left:663px;top:370px;height:46px;padding:0 28px}
.badge{right:14px;top:60px;width:120px;height:90px}
.offer-bar{top:634px;left:0;width:1200px;height:46px;background:var(--navy-deep);color:var(--white);display:flex;align-items:center;justify-content:center;gap:8px;font-size:16px}

/* protect */
.protect-title{left:122px;top:760px;width:520px;font-size:40px;line-height:48px;font-weight:700;color:var(--navy)}
.protect-text{left:122px;top:870px;width:530px;font-size:15px;line-height:30px;color:var(--muted)}
.protect-cta{left:122px;top:1018px;height:44px;padding:0 24px}

/* videos */
.video-card{top:1430px;width:466px;height:264px}
.play{position:absolute;left:50%;top:50%;width:60px;height:60px;margin:-30px 0 0 -30px}

/* reviews */
.reviews{top:1924px;left:0;width:1200px;height:779px}
.reviews-title{position:absolute;top:100px;width:1200px;text-align:center;font-size:46px;font-weight:700;color:var(--white)}
.reviews-sub{position:absolute;top:160px;width:1200px;text-align:center;font-size:20px;color:var(--white)}
.review-card{position:absolute;top:261px;width:282px;height:265px;background:var(--white);border-radius:6px;padding:24px 38px;font-size:15px;line-height:26px;color:var(--navy)}
.stars{color:var(--orange);text-align:center;margin-top:12px;font-size:18px;letter-spacing:2px}
.reviewer{text-align:center;font-weight:700;margin-top:4px}
.avatar{position:absolute;top:562px;width:100px;height:100px;border-radius:50%;border:4px solid var(--white);background:#c3b8ab}
.dots{position:absolute;top:700px;left:0;width:1200px;display:flex;justify-content:center;gap:10px}
.dots span{width:10px;height:10px;border-radius:50%;background:var(--white)}
.dots .on{background:var(--orange)}

/* footer */
.site-footer{top:3787px;left:0;width:1200px;height:563px;background:var(--navy-deep);color:var(--white)}
.f-head{position:absolute;font-weight:700;color:var(--orange);font-size:18px}
.f-head-white{color:var(--white)}
.news-input{position:absolute;left:142px;top:66px;width:220px;height:38px;background:var(--white);border-radius:3px 0 0 3px;font-size:13px;color:#9aa3ad;padding:10px 12px}
.news-btn{position:absolute;left:362px;top:66px;width:130px;height:38px;background:var(--orange);border-radius:0 3px 3px 0;font-weight:600;font-size:14px;display:flex;align-items:center;justify-content:center;gap:6px}
.social{position:absolute;top:66px;left:562px;display:flex;gap:14px}
.social span{width:36px;height:36px;border:2px solid var(--white);border-radius:50%}
.f-call{position:absolute;left:820px;top:70px;font-size:15px;display:flex;align-items:center;gap:8px}
.f-call b{font-size:20px}
.f-rule{position:absolute;left:142px;top:122px;width:916px;height:1px;background:rgba(255,255,255,.25)}
.f-brand{position:absolute;left:142px;top:170px;width:220px;text-align:center}
.f-brand .mark{width:90px;height:90px;border-radius:50%;background:var(--orange);margin:0 auto 12px}
.f-brand .name{font-weight:600;font-size:20px}
.f-about{position:absolute;left:142px;top:310px;width:210px;font-size:13px;line-height:24px;color:#d3dde8}
.f-list{position:absolute;top:240px;list-style:none;font-size:14px;line-height:36px;color:#d3dde8}
.f-list li::before{content:"▸ ";color:var(--white)}
.f-field{position:absolute;left:820px;width:238px;height:32px;background:var(--white);border-radius:2px;font-size:12px;color:#9aa3ad;padding:8px 10px}
.f-send{position:absolute;left:1012px;top:340px;width:46px;height:60px;background:var(--orange);display:flex;align-items:center;justify-content:center}
.copyright{position:absolute;top:495px;width:1200px;text-align:center;font-size:13px;color:#d3dde8}
</style>
</head>
<body>

<header class="site-header abs">
  <div class="brand"><span class="brand-dot"></span>Elder Harbor Circle</div>
  <nav class="main-nav"><span>Products</span><span>How it Works</span><span>Pricing</span><span>Videos</span><span>About Us</span></nav>
  <div class="header-phone">
    <svg width="18" height="18" viewBox="0 0 24 24"><path fill="#f29a1d" d="M6.6 10.8a15 15 0 006.6 6.6l2.2-2.2c.3-.3.7-.4 1-.2 1.1.4 2.3.6 3.6.6.6 0 1 .4 1 1V20c0 .6-.4 1-1 1A17 17 0 013 4c0-.6.4-1 1-1h3.5c.6 0 1 .4 1 1 0 1.3.2 2.5.6 3.6.1.3 0 .7-.2 1z"/></svg>
    1-877-555-0142
  </div>
  <a class="btn btn-solid header-login">Login/Register ➜</a>
</header>

<section class="hero abs">
  <div class="photo" role="img" aria-label="Two white alert pendants with red cross buttons on a soft grey backdrop" style="left:0;top:0;width:1200px;height:552px;background:linear-gradient(100deg,#e9ebed 0%,#d6d9dc 55%,#c9cdd1 100%)"></div>
  <svg class="abs badge" viewBox="0 0 120 90" aria-label="Ranking badge"><path d="M20 10 L120 10 L120 70 L20 70 L34 40 Z" fill="#ffffff" stroke="#d6d9dc"/></svg>
  <h1 class="abs hero-title">Elder Harbor Circle</h1>
  <p class="abs hero-text">Pellentesque habitant morbi tristique senectus et netus et malesuada fames ac turpis egestas. Vestibulum tortor quam, feugiat vitae, eget, tempor sit amet, ante.</p>
  <a class="abs btn btn-solid hero-cta">Contact Us ›</a>
</section>
<div class="offer-bar abs">◷ Limited Time Offer! <b>Call Now To Get 3 Free Months</b></div>

<section>
  <h2 class="abs protect-title">Protect family, health, and independence</h2>
  <p class="abs protect-text">Pellentesque habitant morbi tristique senectus et netus et malesuada fames ac turpis egestas. Vestibulum tortor quam, feugiat vitae, eget, tempor sit amet, ante. Donec eu libero sit amet quam egestas semper. Aenean ultricies mi vitae est. Mauris placerat eleifend leo. Pellentesque habitant morbi tristique senectus et netus et malesuada fames ac turpis egestas.</p>
  <a class="abs btn btn-outline protect-cta">Find Your Solution ›</a>
  <div class="photo" role="img" aria-label="Hand holding a white alert pendant with a red cross button" style="left:654px;top:812px;width:546px;height:365px;background:radial-gradient(ellipse at 40% 50%,#f1f2f3 0%,#d9c3b0 60%,#e8ddd3 100%)"></div>
</section>

<section>
  <h2 class="section-title" style="top:1270px">Check Out Our Most Recent Videos</h2>
  <p class="section-lede" style="top:1318px">In enim justo, rhoncus ut, imperdiet a, venenatis vitae, justo. Nullam dictum felis eu pede mollis pretium. Integer tincidunt. Cras dapibus. Vivamus elementum semper nisi. Aenean vulputate eleifend tellus.</p>
  <div class="photo video-card" role="img" aria-label="Video still of a smiling senior couple" style="left:122px;background:linear-gradient(135deg,#cfe2ea,#e6d6c6)">
    <svg class="play" viewBox="0 0 60 60"><circle cx="30" cy="30" r="28" fill="none" stroke="#2aa9b8" stroke-width="3"/><path d="M24 19 L42 30 L24 41 Z" fill="none" stroke="#2aa9b8" stroke-width="3"/></svg>
  </div>
  <div class="photo video-card" role="img" aria-label="Video still of a smiling senior woman" style="left:613px;background:linear-gradient(135deg,#a9c7a0,#e3d9cc)">
    <svg class="play" viewBox="0 0 60 60"><circle cx="30" cy="30" r="28" fill="none" stroke="#2aa9b8" stroke-width="3"/><path d="M24 19 L42 30 L24 41 Z" fill="none" stroke="#2aa9b8" stroke-width="3"/></svg>
  </div>
  <div class="date-row" style="left:122px;top:1722px"><div class="date">Nov 22<br>2017</div><div class="date-text">Etiam ultricies nisi vel augue. Curabitur ullamcorper<br>ultricies tellus eget condimentum nisi.</div></div>
  <div class="date-row" style="left:613px;top:1722px"><div class="date">Oct 11,<br>2017</div><div class="date-text">Etiam ultricies nisi vel augue. Curabitur ullamcorper<br>ultricies tellus eget condimentum nisi.</div></div>
  <a class="abs btn btn-outline" style="left:500px;top:1820px;height:42px;padding:0 26px">Watch All Videos ›</a>
  <div class="pager" style="left:1005px;top:1824px"><span class="prev"></span><span class="next"></span></div>
</section>

<section class="reviews abs">
  <div class="photo" role="img" aria-label="Senior couple walking outdoors under a dark blue overlay" style="left:0;top:0;width:1200px;height:779px;background:linear-gradient(180deg,#4c5e6b 0%,#5f7257 60%,#405060 100%)"></div>
  <h2 class="reviews-title">REVIEWS</h2>
  <p class="reviews-sub">See what our customers are saying about us</p>
  <svg class="abs" style="left:580px;top:198px" width="40" height="30" viewBox="0 0 40 30"><path d="M2 28V16C2 8 6 3 14 2v6c-4 1-5 4-5 8h5v12zM22 28V16c0-8 4-13 12-14v6c-4 1-5 4-5 8h5v12z" fill="#f29a1d"/></svg>
  <svg class="abs" style="left:20px;top:380px" width="20" height="40" viewBox="0 0 20 40"><path d="M17 2 L3 20 L17 38" fill="none" stroke="#fff" stroke-width="2"/></svg>
  <svg class="abs" style="left:1160px;top:380px" width="20" height="40" viewBox="0 0 20 40"><path d="M3 2 L17 20 L3 38" fill="none" stroke="#fff" stroke-width="2"/></svg>
  <div class="review-card" style="left:145px">Lorem ipsum dolor sit amet, consectetur adipiscing elit. Vivamus commodo libero ac lacus porttitor, eget pretium augue sollicitudin. Maecenas malesuada ante.<div class="stars">★★★★★</div><div class="reviewer">Owen R. Talbrook</div></div>
  <div class="review-card" style="left:462px">Lorem ipsum dolor sit amet, consectetur adipiscing elit. Vivamus commodo libero ac lacus porttitor, eget pretium augue sollicitudin. Maecenas malesuada ante.<div class="stars">★★★★★</div><div class="reviewer">Marcus Whitfield</div></div>
  <div class="review-card" style="left:773px">Lorem ipsum dolor sit amet, consectetur adipiscing elit. Vivamus commodo libero ac lacus porttitor, eget pretium augue sollicitudin. Maecenas malesuada ante.<div class="stars">★★★★★</div><div class="reviewer">Dale Ferrano</div></div>
  <div class="avatar" role="img" aria-label="Reviewer portrait" style="left:236px"></div>
  <div class="avatar" role="img" aria-label="Reviewer portrait" style="left:554px"></div>
  <div class="avatar" role="img" aria-label="Reviewer portrait" style="left:864px"></div>
  <div class="dots"><span class="on"></span><span></span><span></span><span></span></div>
</section>

<section>
  <h2 class="section-title" style="top:2782px">Recent Elder Harbor Circle Articles</h2>
  <p class="section-lede" style="top:2832px">In enim justo, rhoncus ut, imperdiet a, venenatis vitae, justo. Nullam dictum felis eu pede mollis pretium. Integer tincidunt. Cras dapibus. Vivamus elementum semper nisi. Aenean vulputate eleifend tellus.</p>
  <div class="photo" role="img" aria-label="Senior couple paying online with a laptop" style="left:122px;top:2935px;width:468px;height:227px;background:linear-gradient(135deg,#e9e4dc,#cfc2b3)"></div>
  <div class="photo" role="img" aria-label="Smiling senior woman portrait" style="left:613px;top:2935px;width:466px;height:215px;background:linear-gradient(135deg,#f0ebe4,#d8c7b5)"></div>
  <div class="photo" role="img" aria-label="Laughing senior couple" style="left:613px;top:3249px;width:466px;height:215px;background:linear-gradient(135deg,#c8d6be,#e3d2c0)"></div>
  <div class="date-row" style="left:122px;top:3286px"><div class="date">Nov 22<br>2017</div><div class="date-text">Etiam ultricies nisi vel augue. Curabitur ullamcorper<br>ultricies tellus eget condimentum nisi.</div></div>
  <p class="abs" style="left:122px;top:3350px;width:468px;font-size:14px;line-height:28px;color:var(--muted)">Pellentesque habitant morbi tristique senectus et netus et malesuada fames ac turpis egestas. Vestibulum tortor quam, feugiat vitae, eget, tempor sit amet, ante. Donec eu libero sit amet quam egestas semper. Aenean ultricies mi vitae est. Mauris placerat eleifend leo. Pellentesque habitant morbi tristique senectus et netus et malesuada fames ac turpis egestas.</p>
  <div class="date-row" style="left:613px;top:3168px"><div class="date">Nov 22<br>2017</div><div class="date-text">Etiam ultricies nisi vel augue. Curabitur ullamcorper<br>ultricies tellus eget condimentum nisi.</div></div>
  <div class="date-row" style="left:613px;top:3482px"><div class="date">Nov 22<br>2017</div><div class="date-text">Etiam ultricies nisi vel augue. Curabitur ullamcorper<br>ultricies tellus eget condimentum nisi.</div></div>
  <a class="abs btn btn-outline" style="left:510px;top:3592px;height:42px;padding:0 26px">Read more articles ›</a>
  <div class="pager" style="left:1005px;top:3596px"><span class="prev"></span><span class="next"></span></div>
</section>

<footer class="site-footer abs">
  <div class="f-head" style="left:142px;top:26px">Subscribe to our Newsletter</div>
  <div class="news-input">Your email address</div>
  <div class="news-btn">➤ SUBSCRIBE</div>
  <div class="f-head" style="left:562px;top:26px">Follow us on</div>
  <div class="social"><span></span><span></span><span></span><span></span></div>
  <div class="f-head" style="left:820px;top:26px">Need Help?</div>
  <div class="f-call">
    <svg width="16" height="16" viewBox="0 0 24 24"><path fill="#fff" d="M6.6 10.8a15 15 0 006.6 6.6l2.2-2.2c.3-.3.7-.4 1-.2 1.1.4 2.3.6 3.6.6.6 0 1 .4 1 1V20c0 .6-.4 1-1 1A17 17 0 013 4c0-.6.4-1 1-1h3.5c.6 0 1 .4 1 1 0 1.3.2 2.5.6 3.6.1.3 0 .7-.2 1z"/></svg>
    CALL US <b>1-877-555-0142</b>
  </div>
  <div class="f-rule"></div>
  <div class="f-brand"><div class="mark"></div><div class="name">Elder Harbor Circle</div></div>
  <p class="f-about">Lorem ipsum dolor sit amet, consectetur adipiscing elit. Cras orci sem, vulputate sit amet ipsum vel ex et.</p>
  <div class="f-head f-head-white" style="left:405px;top:200px">Information</div>
  <ul class="f-list" style="left:420px"><li>Blog</li><li>Videos</li><li>Code of Ethics</li><li>Affiliate Program</li><li>FAQ</li></ul>
  <div class="f-head f-head-white" style="left:612px;top:200px">Useful Links</div>
  <ul class="f-list" style="left:612px"><li>Customer Service</li><li>Order Online</li><li>Refer a friend</li><li>Contact Us</li><li>Site Map</li></ul>
  <div class="f-head f-head-white" style="left:820px;top:200px">Get in Touch</div>
  <div class="f-field" style="top:244px">Name</div>
  <div class="f-field" style="top:290px">Email address</div>
  <div class="f-field" style="top:340px;width:192px;height:60px">Message</div>
  <div class="f-send"><svg width="18" height="18" viewBox="0 0 24 24"><path fill="#fff" d="M2 21l21-9L2 3v7l15 2-15 2z"/></svg></div>
  <div class="copyright">Elder Harbor Circle. Copyright © 2017. All rights reserved.</div>
</footer>

</body>
</html>
```